Harlowe plumbing business cards

Want a functional designed for my business cards using my logo

Company Name- Harlowe Plumbing, Heating & Water Systems
Name- Marcus Harlowe
Title- Vice President
Cell- 555-318-7426
Email- Harloweplumbing@mailbrook.net
Business address-
PO Box 37
Fenwick Mill, MD 21999

Industry/Entity Type

Plumbing

```html
<!DOCTYPE html>
<html lang="en">
<head>
<meta charset="utf-8">
<title>Harlowe Plumbing business cards</title>
<link rel="stylesheet" href="https://fonts.googleapis.com/css2?family=Didact+Gothic&family=Montserrat:wght@700&display=swap">
<style>
  :root {
    --backdrop: #5b5d60;
    --card: #3a3a3b;
    --blue: #1f6fc0;
    --white: #ffffff;
    --silver: #b9bcc0;
    --band: #9db7e3;
    --rule: #1f6fc0;
  }
  * { box-sizing: border-box; margin: 0; padding: 0; }
  html, body { width: 1200px; height: 960px; overflow: hidden; }
  body {
    background: radial-gradient(ellipse at 50% 40%, #6a6c70 0%, var(--backdrop) 55%, #3e4043 100%);
    font-family: "Didact Gothic", sans-serif;
    position: relative;
  }
  .card {
    position: absolute;
    width: 640px;
    height: 366px;
    background: var(--card);
    box-shadow: 0 18px 40px rgba(0,0,0,.45);
    overflow: hidden;
  }
  .card--back { left: 70px; top: 60px; }
  .card--front { left: 490px; top: 520px; }

  .brand { position: absolute; display: flex; align-items: center; gap: 16px; }
  .brand__mark { flex: none; }
  .brand__name { line-height: 1.1; }
  .brand__line { display: block; white-space: nowrap; }

  .card--back .brand {
    left: 0; right: 0; top: 130px;
    justify-content: center;
    color: var(--silver);
    font-size: 34px;
  }
  .card--back .brand__mark { width: 72px; height: 72px; background: #4a4b4d; }

  .card--front .brand {
    left: 40px; top: 126px;
    color: var(--white);
    font-size: 26px;
  }
  .card--front .brand__mark { width: 56px; height: 56px; background: #4a5a70; }

  .person { position: absolute; right: 40px; top: 30px; text-align: right; }
  .person__name {
    font-family: "Montserrat", sans-serif; font-weight: 700;
    color: var(--blue); font-size: 26px; letter-spacing: .5px;
  }
  .person__title { color: var(--white); font-size: 20px; margin-top: 2px; }

  .rule { position: absolute; height: 2px; background: var(--rule); }
  .rule--top { top: 108px; left: 330px; right: 40px; }
  .rule--mid { top: 246px; left: 40px; width: 300px; }

  .hotline {
    position: absolute; left: 40px; top: 192px;
    color: var(--blue); font-size: 36px; letter-spacing: 1px; line-height: 1.1;
  }
  .contact { position: absolute; left: 40px; top: 256px; list-style: none; }
  .contact li { display: flex; align-items: center; gap: 12px; color: var(--white); font-size: 18px; height: 30px; }
  .contact svg { width: 20px; height: 20px; fill: var(--blue); flex: none; }

  .address {
    position: absolute; right: 40px; top: 258px; text-align: right;
    color: var(--white); font-size: 18px; line-height: 1.45; font-style: normal;
  }
  .band {
    position: absolute; left: 0; right: 0; bottom: 0; height: 34px;
    background: var(--band);
  }
</style>
</head>
<body>
  <section class="card card--back" aria-label="Card back">
    <div class="brand">
      <span class="brand__mark" aria-hidden="true"></span>
      <p class="brand__name">
        <span class="brand__line">Harlowe Plumbing</span>
        <span class="brand__line">Heating &amp; Water Systems</span>
      </p>
    </div>
  </section>

  <section class="card card--front" aria-label="Card front">
    <div class="person">
      <p class="person__name">Marcus Harlowe</p>
      <p class="person__title">Vice President</p>
    </div>
    <div class="rule rule--top"></div>

    <div class="brand">
      <span class="brand__mark" aria-hidden="true"></span>
      <p class="brand__name">
        <span class="brand__line">Harlowe Plumbing</span>
        <span class="brand__line">Heating &amp; Water Systems</span>
      </p>
    </div>

    <p class="hotline">555.204.6613</p>
    <div class="rule rule--mid"></div>

    <ul class="contact">
      <li>
        <svg viewBox="0 0 24 24" aria-hidden="true"><path d="M6.6 10.8a15.1 15.1 0 0 0 6.6 6.6l2.2-2.2c.3-.3.7-.4 1-.2 1.1.4 2.3.6 3.6.6.6 0 1 .4 1 1V20c0 .6-.4 1-1 1C10.6 21 3 13.4 3 4c0-.6.4-1 1-1h3.5c.6 0 1 .4 1 1 0 1.3.2 2.5.6 3.6.1.3 0 .7-.2 1z"/></svg>
        555-318-7426
      </li>
      <li>
        <svg viewBox="0 0 24 24" aria-hidden="true"><path d="M2 5h20v14H2z M3.5 6.5 12 13l8.5-6.5" stroke="#3a3a3b" stroke-width="1.4"/></svg>
        Harloweplumbing@mailbrook.net
      </li>
    </ul>

    <address class="address">
      PO Box 37<br>
      Fenwick Mill, MD 21999
    </address>

    <div class="band" role="img" aria-label="Light blue band with a bubble pattern"></div>
  </section>
</body>
</html>
```